WhenWeWeighTheMatter.com, a blog on economics and social issues, needs a facelift.

Make my blog website more attractive and functional.
It needs a cover image. The purpose of the blog is to sort out errors the public discourse on current topics that affect timeless issues. It is to correct erroneous conclusions on public issues caused by ignoring relevant facts, misunderstandings of the facts upon which they base conclusions, and/or misanalysis of the facts. The topics vary widely.

I have in mind some kind of transition from an out of focus area to a focused area. At one time I used the attached image, but it gave no hint of a transition from a lack of clarity to clarity. I am wide open to other approaches to conveying that idea.

A particular improvement would be making the Subscribe button to be easier to find,

Target Market(s)

People interested in how timeless economic, social, constitutional, political philosophy, and governance ideals apply to current affairs.

Logo Text

While I would not rule it out, I don't have in mind that the logo will be different from the cover image. The essence of the blog is mostly captured by its name, When We Weigh The Matter.

Requirements
Must have
• Cover image. Webpages that are nice looking and appropriate to the seriousness of the blog.

FOLLOW and SHARE buttons in easily found places.
Nice to have
• Instructions as to how to transfer/set up what I receive from the designer to the WordPress website.

Suggestions on Fonts.

Suggested changes to the pages.

BTW: I had no help setting up the current page.
Should not have
• Anything that hints that I am interested in or facilitiates the receipt of money from followers.

```html
<!DOCTYPE html>
<html lang="en">
<head>
<meta charset="utf-8">
<title>When We Weigh The Matter</title>
<link href="https://fonts.googleapis.com/css2?family=IBM+Plex+Sans:wght@400;500;600;700&family=Open+Sans:wght@400;600;700&display=swap" rel="stylesheet">
<style>
:root{
  --page:#f6f1f1;
  --white:#ffffff;
  --ink:#1d1d1d;
  --text:#3d3d3d;
  --muted:#666666;
  --blue:#1a8de0;
  --blue-dark:#1b6fc4;
  --rule:#bdbdbd;
  --line:#e4e4e4;
  --footer:#222222;
  --footer-text:#d8d8d8;
}
*{margin:0;padding:0;box-sizing:border-box}
html,body{width:1200px;height:4030px;overflow:hidden}
body{position:relative;background:var(--page);font-family:"Open Sans",Arial,sans-serif;color:var(--text)}

/* hero */
.hero{position:absolute;left:0;top:0;width:1200px;height:505px;overflow:hidden}
.hero-photo{position:absolute;inset:0;background:
  radial-gradient(ellipse at 60% 20%,rgba(250,200,130,.85),transparent 55%),
  linear-gradient(180deg,#c78a4e 0%,#9a6236 35%,#5b3a24 70%,#2c1d14 100%)}
.hero-shade{position:absolute;inset:0;background:rgba(0,0,0,.18)}
.brand{position:absolute;left:131px;top:28px;color:var(--white)}
.brand-name{font-family:"IBM Plex Sans",Arial,sans-serif;font-weight:600;font-size:25px;letter-spacing:.5px;text-transform:uppercase}
.brand-tag{font-size:13px;margin-top:-1px}
.nav{position:absolute;top:33px;left:834px;display:flex;gap:37px}
.nav a{color:var(--white);text-decoration:none;font-family:"IBM Plex Sans",Arial,sans-serif;font-weight:500;font-size:14px}
.hero-label{position:absolute;left:533px;top:197px;width:140px;height:33px;border:2px solid var(--white);color:var(--white);font-family:"IBM Plex Sans",Arial,sans-serif;font-size:14px;font-weight:500;display:flex;align-items:center;justify-content:center}
.hero-title{position:absolute;left:300px;width:600px;top:254px;text-align:center;color:var(--white);font-family:"IBM Plex Sans",Arial,sans-serif;font-weight:600;font-size:31px;line-height:40px;text-transform:uppercase}
.dots{position:absolute;top:428px;left:556px;display:flex;gap:11px;align-items:center}
.dots span{width:8px;height:8px;border-radius:50%;background:var(--white)}
.dots .active{width:13px;height:13px;background:transparent;border:2px solid #e8432e}
.side-actions{position:absolute;right:0;top:205px;display:flex;flex-direction:column;gap:11px}
.side-actions a{width:131px;height:33px;background:var(--blue);color:var(--white);text-decoration:none;font-family:"IBM Plex Sans",Arial,sans-serif;font-weight:600;font-size:14px;display:flex;align-items:center;padding-left:16px;gap:9px}
.side-actions svg{width:13px;height:13px;fill:var(--white)}

/* featured */
.section-title{font-family:"IBM Plex Sans",Arial,sans-serif;font-weight:700;color:var(--ink);text-transform:uppercase}
.featured-title{position:absolute;left:131px;top:543px;font-size:22px}
.title-rule{position:absolute;height:3px;width:42px;background:var(--rule)}
.posts{position:absolute;left:133px;top:613px;width:670px;display:flex;flex-direction:column;gap:68px}
.post{position:relative;height:203px}
.post-thumb{position:absolute;left:0;top:0;width:247px;height:203px}
.post-body{position:absolute;left:277px;top:0;width:390px;height:203px}
.post-meta{font-size:10.5px;color:var(--text)}
.post-meta b{font-weight:400;margin:0 8px}
.post-title{font-family:"IBM Plex Sans",Arial,sans-serif;font-weight:700;font-size:13.5px;line-height:22px;color:var(--ink);text-transform:uppercase;margin-top:9px;width:350px}
.post-excerpt{font-size:11.8px;line-height:18.2px;color:#444;margin-top:9px;width:372px;max-height:92px;overflow:hidden}
.read-more{position:absolute;left:0;top:195px;font-family:"IBM Plex Sans",Arial,sans-serif;font-weight:700;font-size:11px;color:var(--blue);text-decoration:none;transform:translateY(-50%)}
.read-more::before{content:"";position:absolute;left:0;top:-8px;width:32px;height:2px;background:var(--blue)}
.comment-btn{position:absolute;left:231px;top:182px;width:116px;height:25px;border:1px solid #a8a8a8;background:var(--white);font-size:10.5px;color:#555;display:flex;align-items:center;justify-content:center;gap:4px}
.comment-btn svg{width:10px;height:10px;stroke:#555;fill:none;stroke-width:1.4}
.view-more{position:absolute;left:135px;top:3051px;width:621px;height:48px;border:3px solid var(--blue-dark);color:var(--blue-dark);font-family:"IBM Plex Sans",Arial,sans-serif;font-weight:700;font-size:16px;display:flex;align-items:center;justify-content:center;background:transparent;text-decoration:none}

/* sidebar */
.side-title{position:absolute;left:826px;font-size:15px;font-weight:600}
.side-box{position:absolute;left:826px;width:243px;background:var(--white)}
.side-list{list-style:none;padding:8px 13px 0 13px}
.side-item{display:flex;gap:14px;padding:11px 0 12px 9px;border-bottom:1px solid var(--line);height:139px}
.side-item:last-child{border-bottom:none}
.side-item > div{width:170px}
.side-num{font-family:"IBM Plex Sans",Arial,sans-serif;font-size:13px;color:var(--ink);padding-top:3px}
.side-head{font-family:"IBM Plex Sans",Arial,sans-serif;font-size:13px;line-height:17px;color:var(--ink);text-transform:uppercase}
.side-text{font-size:10px;line-height:14.5px;color:#555;margin-top:6px}
.archive-list{list-style:none;padding:20px 0 0 31px}
.archive-list li{font-size:12.5px;height:30.35px;color:var(--ink)}

/* latest blog */
.blog{position:absolute;left:0;top:3185px;width:1200px;height:496px;background:var(--white)}
.blog-title{position:absolute;left:128px;top:53px;font-size:22px}
.cards{position:absolute;left:134px;top:118px;display:flex;gap:17px}
.card{width:223px;height:327px;border:2px solid #dcdcdc;background:var(--white);position:relative}
.card-photo{height:165px}
.card-date{position:absolute;left:20px;top:154px;background:var(--white);padding:2px 14px 0 8px;font-size:10.5px;font-style:italic;color:var(--ink)}
.card-body{padding:22px 18px 0 20px}
.card-title{font-family:"IBM Plex Sans",Arial,sans-serif;font-size:12.5px;line-height:19px;color:var(--ink);text-transform:uppercase}
.card-text{font-size:9.5px;line-height:14px;color:#444;margin-top:8px}

/* footer */
.footer{position:absolute;left:0;top:3681px;width:1200px;height:349px;background:var(--footer);color:var(--footer-text)}
.footer-brand{position:absolute;left:130px;top:112px;color:var(--white)}
.footer-brand .brand-tag{color:#cfcfcf}
.footer-divider{position:absolute;left:613px;top:72px;width:1px;height:180px;background:#444}
.footer-col-title{font-family:"IBM Plex Sans",Arial,sans-serif;font-weight:700;font-size:13px;color:var(--white)}
.footer-menu{position:absolute;left:751px;top:51px}
.footer-menu ul{list-style:none;margin-top:19px}
.footer-menu li{font-size:12px;height:20px;color:var(--footer-text)}
.footer-follow{position:absolute;left:968px;top:51px}
.follow-list{list-style:none;margin-top:18px}
.follow-list li{display:flex;align-items:center;gap:12px;height:50px;font-size:11.5px;line-height:14px;color:var(--footer-text)}
.follow-dot{width:24px;height:24px;border-radius:50%;background:var(--white);flex:none}
.copyright{position:absolute;left:0;width:1200px;top:310px;text-align:center;font-size:10px;color:#c8c8c8}
</style>
</head>
<body>

<header class="hero">
  <div class="hero-photo" role="img" aria-label="Warm sunset view over a dense city skyline with tall towers"></div>
  <div class="hero-shade"></div>
  <div class="brand">
    <div class="brand-name">When We Weigh The Matter</div>
    <div class="brand-tag">A place to seek clarity on timeless issues and issues of the day.</div>
  </div>
  <nav class="nav"><a href="#">HOME</a><a href="#">ABOUT</a><a href="#">CONTACT</a></nav>
  <div class="hero-label">LATEST POSTS</div>
  <h1 class="hero-title">What’s Going On? – Part VII Black Lives Do Matter, Dashed Hopes</h1>
  <div class="dots"><span></span><span></span><span class="active"></span><span></span><span></span></div>
  <div class="side-actions">
    <a href="#"><svg viewBox="0 0 16 16"><path d="M8 14.5 1.8 8.4A3.7 3.7 0 0 1 8 3.6a3.7 3.7 0 0 1 6.2 4.8z"/></svg>FOLLOW</a>
    <a href="#"><svg viewBox="0 0 16 16"><circle cx="12.5" cy="3" r="2.5"/><circle cx="3.5" cy="8" r="2.5"/><circle cx="12.5" cy="13" r="2.5"/><path d="M3.5 8 12.5 3M3.5 8l9 5" stroke="#fff" stroke-width="1.5"/></svg>SHARE</a>
    <a href="#"><svg viewBox="0 0 16 16"><path d="M1 3h14v1.2L8 9 1 4.2z"/><path d="M1 5.8 8 10.6l7-4.8V13H1z"/></svg>SUBSCRIBE</a>
  </div>
</header>

<h2 class="section-title featured-title">Featured Posts</h2>
<div class="title-rule" style="left:131px;top:577px"></div>

<main class="posts">
  <article class="post">
    <div class="post-thumb" role="img" aria-label="Photo of a statesman speaking at a desk with microphones" style="background:linear-gradient(135deg,#4a3a30,#8a7564 55%,#2d2622)"></div>
    <div class="post-body">
      <div class="post-meta">August 29, 2020<b>|</b>Warren Calloway</div>
      <h3 class="post-title">What’s Going On? – Part V Black Lives Do Matter, Unfair Discriminatory Structures</h3>
      <p class="post-excerpt">Part III and Part IV” of this series reviewed 1) the tremendous progress that blacks in America were making before the War On Poverty (“WOP”) began — despite very high levels of racism and racist laws that intentionally impeded black progress.</p>
      <a class="read-more" href="#">READ MORE</a>
      <div class="comment-btn"><svg viewBox="0 0 10 10"><path d="M1 9V2h5M4 6l5-5"/></svg>Leave a comment</div>
    </div>
  </article>
  <article class="post">
    <div class="post-thumb" role="img" aria-label="Red suspension bridge over blue bay with city behind" style="background:linear-gradient(160deg,#7fa6c9,#3f6f99 45%,#a2392a 60%,#2c5677)"></div>
    <div class="post-body">
      <div class="post-meta">August 29, 2020<b>|</b>Warren Calloway</div>
      <h3 class="post-title">Another California Bust</h3>
      <p class="post-excerpt" style="max-height:110px">Last year, California passed a law[i] that went into effect in January that deemed ride-hailing drivers to be employees (as opposed to independent contractors, as they had been in California and are still in most places). Unable to get a court to strike down the law, RideNow and Hoppa are suspending operations in CA starting next Friday.</p>
      <a class="read-more" href="#">READ MORE</a>
      <div class="comment-btn"><svg viewBox="0 0 10 10"><path d="M1 9V2h5M4 6l5-5"/></svg>Leave a comment</div>
    </div>
  </article>
  <article class="post">
    <div class="post-thumb" role="img" aria-label="Waterfront city and harbour at sunset" style="background:linear-gradient(180deg,#3e6fa6,#d99b4c 45%,#2f5a7c 60%,#1f3d5a)"></div>
    <div class="post-body">
      <div class="post-meta">August 29, 2020<b>|</b>Warren Calloway</div>
      <h3 class="post-title">What’s Going On? – Part IV Black Lives Do Matter,Do-Gooders’ War On Poverty</h3>
      <p class="post-excerpt">This post adds yet another extreme example to the list of posts in this blog[i] that discuss well-intended, insufficiently informed people (“Do-Gooders”) advancing policies and ideas that do more harm than good for the people the Do-Gooders want to help.</p>
      <a class="read-more" href="#">READ MORE</a>
      <div class="comment-btn"><svg viewBox="0 0 10 10"><path d="M1 9V2h5M4 6l5-5"/></svg>Leave a comment</div>
    </div>
  </article>
  <article class="post">
    <div class="post-thumb" role="img" aria-label="City skyline at dusk with mountains behind" style="background:linear-gradient(180deg,#2c3f62,#c8694a 45%,#3a2f48 65%,#121a2c)"></div>
    <div class="post-body">
      <div class="post-meta">August 29, 2020<b>|</b>Warren Calloway</div>
      <h3 class="post-title">What’s Going On? – Part III Black Lives Do Matter, The “Do-Gooders’” Slate</h3>
      <p class="post-excerpt">People who believe that black lives don’t matters deserve all the condemnation they get from their fellow Americans. Thankfully, however, racist Americans (people who believe black lives don’t matter,</p>
      <a class="read-more" href="#">READ MORE</a>
      <div class="comment-btn"><svg viewBox="0 0 10 10"><path d="M1 9V2h5M4 6l5-5"/></svg>Leave a comment</div>
    </div>
  </article>
  <article class="post">
    <div class="post-thumb" role="img" aria-label="Businessman on a phone call at a desk with laptop" style="background:linear-gradient(135deg,#d9d4c8,#8aa1b8 50%,#5d6e7e)"></div>
    <div class="post-body">
      <div class="post-meta">August 29, 2020<b>|</b>Warren Calloway</div>
      <h3 class="post-title">What’s Going On? – Part II Black Lives Do Matter, Problems Aplenty</h3>
      <p class="post-excerpt">A disproportionately high number of severe and intractable problems beset Black Americans. The survival of America’s experiment to establish a government on the proposition that all men are created equal may come to an end if</p>
      <a class="read-more" href="#">READ MORE</a>
      <div class="comment-btn"><svg viewBox="0 0 10 10"><path d="M1 9V2h5M4 6l5-5"/></svg>Leave a comment</div>
    </div>
  </article>
  <article class="post">
    <div class="post-thumb" role="img" aria-label="Close portrait of a man speaking at a hearing" style="background:linear-gradient(135deg,#2a2522,#7b5f52 50%,#1c1a19)"></div>
    <div class="post-body">
      <div class="post-meta">August 29, 2020<b>|</b>Warren Calloway</div>
      <h3 class="post-title">From A Formerly Respected Newspaper.</h3>
      <p class="post-excerpt" style="max-height:110px">This is what showed up in my inbox from The Capital Courier this morning. I suspect no commentary needs to be added for my readers to know what is wrong about this picture. Suffice it to say, with this kind of representation of the facts, CapCourier is not earning its special free press rights.</p>
      <a class="read-more" href="#">READ MORE</a>
      <div class="comment-btn"><svg viewBox="0 0 10 10"><path d="M1 9V2h5M4 6l5-5"/></svg>Leave a comment</div>
    </div>
  </article>
  <article class="post">
    <div class="post-thumb" role="img" aria-label="Businessman in glasses seated in a night city office" style="background:linear-gradient(135deg,#1d3550,#5f86ad 50%,#1a2433)"></div>
    <div class="post-body">
      <div class="post-meta">August 29, 2020<b>|</b>Warren Calloway</div>
      <h3 class="post-title" style="width:385px">Stridewell’ Mistake—Supporting A Counterproductive Cause Against Police</h3>
      <p class="post-excerpt">By picking Calvin Kessler as its newest ‘Run Your Race’ star,” Stridewell has, in a huge way, supported Kessler’s policy prescriptions, rhetoric, and tactics, and, by inference, those of Equal Streets Movement (“ESM”).</p>
      <a class="read-more" href="#">READ MORE</a>
      <div class="comment-btn"><svg viewBox="0 0 10 10"><path d="M1 9V2h5M4 6l5-5"/></svg>Leave a comment</div>
    </div>
  </article>
  <article class="post">
    <div class="post-thumb" role="img" aria-label="Man standing on a glowing platform above a blue city" style="background:linear-gradient(180deg,#4f7fb0,#2b4f78 50%,#8fb7d9 80%,#1f3550)"></div>
    <div class="post-body">
      <div class="post-meta">August 29, 2020<b>|</b>Warren Calloway</div>
      <h3 class="post-title">Exploitation—Part IV (E), Exploiting Exploitation–Additional Negative Effects</h3>
      <p class="post-excerpt">As was explained in Exploitation Part IV (d), the most self-defeating effect of the anti-sweatshop movement was that it slowed the progress of impoverished countries along their path to prosperity.</p>
      <a class="read-more" href="#">READ MORE</a>
      <div class="comment-btn"><svg viewBox="0 0 10 10"><path d="M1 9V2h5M4 6l5-5"/></svg>Leave a comment</div>
    </div>
  </article>
  <article class="post">
    <div class="post-thumb" role="img" aria-label="Double exposure of a businessman and city towers" style="background:linear-gradient(135deg,#f2efea,#b7bcc4 45%,#5b6673 75%,#d8d6d2)"></div>
    <div class="post-body">
      <div class="post-meta">August 29, 2020<b>|</b>Warren Calloway</div>
      <h3 class="post-title">Exploitation—Part IV (D), Exploiting Exploitation–The Effects</h3>
      <p class="post-excerpt">In Exploitation Part IV chapters (a), (b), and (c), I claimed the anti-sweatshop movement inflicted much misery on poor people around the world. With the foundation laid in those chapters,</p>
      <a class="read-more" href="#">READ MORE</a>
      <div class="comment-btn"><svg viewBox="0 0 10 10"><path d="M1 9V2h5M4 6l5-5"/></svg>Leave a comment</div>
    </div>
  </article>
</main>

<a class="view-more" href="#">VIEW MORE POSTS</a>

<aside>
  <h2 class="section-title side-title" style="top:545px">Related Posts</h2>
  <div class="title-rule" style="left:826px;top:577px;width:38px"></div>
  <div class="side-box" style="top:607px;height:560px">
    <ol class="side-list">
      <li class="side-item"><span class="side-num">01</span><div><div class="side-head">Hurricane Harvey and me</div><p class="side-text">Author’s Note: Unlike my typical posts, this post is not about ideas and policies (although I have snuck in a few).</p></div></li>
      <li class="side-item"><span class="side-num">02</span><div><div class="side-head">Prelude to a post about the Florida Shooting – A growing leftist trend</div><p class="side-text">I was writing a post about the possible nexus between the leftist school policies</p></div></li>
      <li class="side-item"><span class="side-num">03</span><div><div class="side-head">An example of fake fact checking</div><p class="side-text">On January 12 FACTMETER weighed in on the controversy discussed in my last post, “A Prime Example of Fake News.”</p></div></li>
      <li class="side-item"><span class="side-num">04</span><div><div class="side-head">Non sequiturs on parade – Part VI</div><p class="side-text">Let’s continue analyzing Stan Rolfe’s handy compilation of leftist bromides, non sequiturs, self-congratulations, and just</p></div></li>
    </ol>
  </div>

  <h2 class="section-title side-title" style="top:1201px">Archives</h2>
  <div class="title-rule" style="left:826px;top:1223px;width:38px"></div>
  <div class="side-box" style="top:1232px;height:500px">
    <ul class="archive-list">
      <li>October 2020</li><li>September 2020</li><li>August 2020</li><li>July 2020</li><li>June 2020</li><li>May 2020</li><li>April 2020</li><li>March 2020</li><li>February 2020</li><li>January 2020</li><li>December 2019</li><li>November 2019</li><li>October 2019</li><li>September 2019</li><li>August 2019</li>
    </ul>
  </div>

  <h2 class="section-title side-title" style="top:1772px">Latest Posts</h2>
  <div class="title-rule" style="left:826px;top:1801px;width:38px"></div>
  <div class="side-box" style="top:1810px;height:560px">
    <ol class="side-list">
      <li class="side-item"><span class="side-num">01</span><div><div class="side-head">Hurricane Harvey and me</div><p class="side-text">Author’s Note: Unlike my typical posts, this post is not about ideas and policies (although I have snuck in a few).</p></div></li>
      <li class="side-item"><span class="side-num">02</span><div><div class="side-head">Prelude to a post about the Florida Shooting – A growing leftist trend</div><p class="side-text">I was writing a post about the possible nexus between the leftist school policies</p></div></li>
      <li class="side-item"><span class="side-num">03</span><div><div class="side-head">An example of fake fact checking</div><p class="side-text">On January 12 FACTMETER weighed in on the controversy discussed in my last post, “A Prime Example of Fake News.”</p></div></li>
      <li class="side-item"><span class="side-num">04</span><div><div class="side-head">Non sequiturs on parade – Part VI</div><p class="side-text">Let’s continue analyzing Stan Rolfe’s handy compilation of leftist bromides, non sequiturs, self-congratulations, and just</p></div></li>
    </ol>
  </div>
</aside>

<section class="blog">
  <h2 class="section-title blog-title">Latest Blog</h2>
  <div class="title-rule" style="left:128px;top:88px"></div>
  <div class="cards">
    <article class="card">
      <div class="card-photo" role="img" aria-label="Two businesspeople shaking hands" style="background:linear-gradient(135deg,#2a3f5e,#a9b8c8 55%,#eef1f4)"></div>
      <span class="card-date">September 27, 2020</span>
      <div class="card-body"><h3 class="card-title">What’s Going On? – Part VII Black Lives Do Matter, Dashed Hopes</h3><p class="card-text">Parts I – VI[i] of this series described mostly well-intended policies that harmed Blacks and produced valid grievances.</p></div>
    </article>
    <article class="card">
      <div class="card-photo" role="img" aria-label="Businessman in a suit and tie among office towers" style="background:linear-gradient(135deg,#e8e8e8,#9aa4ae 50%,#33404e)"></div>
      <span class="card-date">September 27, 2020</span>
      <div class="card-body"><h3 class="card-title">/The Feed Paradox – A Review</h3><p class="card-text">Reelhouse’s /The Feed Paradox, an exposé on social media, is informative and important. [It does not, however, absolve Reelhouse of its public</p></div>
    </article>
    <article class="card">
      <div class="card-photo" role="img" aria-label="Man walking toward a bright sunrise between city towers" style="background:linear-gradient(180deg,#f0b66a,#c56a3c 40%,#3a3f4e 75%,#1e222c)"></div>
      <span class="card-date">September 27, 2020</span>
      <div class="card-body"><h3 class="card-title">What’s Going On? – Part VI Black Lives Do Matter, The Stereotyping Problem</h3><p class="card-text">In Part II, Part III, Part IV, and Part V of this series, we sorted out many of the grievances Blacks can legitimately lodge against US</p></div>
    </article>
    <article class="card">
      <div class="card-photo" role="img" aria-label="Businessman working at a laptop in a bright office" style="background:linear-gradient(135deg,#cfd8e2,#6f8399 50%,#273446)"></div>
      <span class="card-date">September 27, 2020</span>
      <div class="card-body"><h3 class="card-title">What’s Going On? – Part VII Black Lives Do Matter, Dashed Hopes</h3><p class="card-text">Parts I – VI[i] of this series described mostly well-intended policies that harmed Blacks and produced valid grievances.</p></div>
    </article>
  </div>
</section>

<footer class="footer">
  <div class="footer-brand">
    <div class="brand-name">When We Weigh The Matter</div>
    <div class="brand-tag">A place to seek clarity on timeless issues and issues of the day.</div>
  </div>
  <div class="footer-divider"></div>
  <div class="footer-menu">
    <div class="footer-col-title">MENU</div>
    <ul><li>HOME</li><li>ABOUT US</li><li>CONTACT US</li></ul>
  </div>
  <div class="footer-follow">
    <div class="footer-col-title">FOLLOW US</div>
    <ul class="follow-list">
      <li><span class="follow-dot"></span><span>Like us on<br>CIRCLEBOOK</span></li>
      <li><span class="follow-dot"></span><span>Follow us on<br>CHIRPER</span></li>
      <li><span class="follow-dot"></span><span>Follow us on<br>PROLINKS</span></li>
    </ul>
  </div>
  <div class="copyright">Copyright © 2020 All Rights Reserved</div>
</footer>

</body>
</html>
```